Larkspur Ridge Management - Business Cards

I need business cards. My current logo was designed by a designer at this site and I very much like and am happy with the results. I would like a business card that is trendy, unique, current yet professional. I deal with high net worth clients daily

Target Market(s)

Out of state investors looking to get into the rental market in Ohio

Industry/Entity Type

Property Management, Consulting

Contact Information for Business Card

Name, Title (Chief Financial Officer) office phone number (555) 817-3094 website address larkridgemgmt.example

Font styles to use
Sans Serif

Colors
0054AA
0677BA
7BADD7
CADEEF
E8F1F8
0094D4
00A9DD
6FCCEA
C7EBF8
E9F6FB
00AB8E
00BBA5
67D7C9
C6EFE9
E9F9F6

```html
<!DOCTYPE html>
<html lang="en">
<head>
<meta charset="utf-8">
<title>Larkspur Ridge Management – Business Cards</title>
<link href="https://fonts.googleapis.com/css2?family=Outfit:wght@300;400;700&display=swap" rel="stylesheet">
<style>
  :root {
    --bg: #2f2f31;
    --card-white: #ffffff;
    --navy: #1f3464;
    --slate: #58585b;
    --red: #cf2630;
    --ink: #2a2a2e;
  }
  * { box-sizing: border-box; margin: 0; padding: 0; }
  html, body { width: 1200px; height: 900px; overflow: hidden; }
  body {
    background: var(--bg);
    font-family: "Outfit", sans-serif;
    position: relative;
  }
  .card {
    position: absolute;
    left: 320px;
    width: 560px;
    height: 320px;
    border-radius: 22px;
    overflow: hidden;
  }
  .card--front { top: 100px; background: var(--card-white); }
  .card--back { top: 480px; background: var(--red); }

  .edge-band {
    position: absolute; left: 0; top: 0; bottom: 0; width: 24px;
    display: flex; flex-direction: column;
  }
  .edge-band__navy { flex: 0 0 66%; background: var(--navy); }
  .edge-band__gap { flex: 0 0 4px; background: var(--card-white); }
  .edge-band__slate { flex: 1; background: var(--slate); }

  .name-tab {
    position: absolute; left: 24px; top: 44px;
    width: 12px; height: 30px; background: var(--navy);
    border-radius: 0 6px 6px 0;
  }

  .identity { position: absolute; left: 56px; top: 42px; }
  .identity__name {
    font-weight: 700; font-size: 30px; color: var(--navy);
    letter-spacing: 0.5px; text-transform: uppercase; line-height: 1.1;
  }
  .identity__title {
    font-weight: 300; font-size: 17px; color: var(--ink); margin-top: 2px;
  }
  .identity__rule {
    width: 120px; height: 2px; background: var(--ink); margin: 14px 0 16px -10px;
  }

  .contact-list { list-style: none; margin-left: -14px; }
  .contact-list__item {
    display: flex; align-items: center; gap: 10px;
    font-size: 16px; font-weight: 300; color: var(--ink);
    margin-bottom: 7px;
  }
  .contact-list__icon { width: 16px; height: 16px; flex: 0 0 16px; }

  .brand-mark {
    position: absolute; right: 46px; top: 190px;
    display: flex; align-items: center; gap: 10px;
  }
  .brand-mark__square { width: 14px; height: 14px; background: var(--navy); }
  .brand-mark__name {
    font-weight: 700; font-size: 18px; color: var(--navy);
    text-transform: uppercase; letter-spacing: 0.5px; line-height: 1.15;
  }

  .card--back .brand-mark {
    position: absolute; left: 0; right: 0; top: 0; bottom: 0;
    justify-content: center;
  }
  .card--back .brand-mark__square { background: var(--card-white); width: 18px; height: 18px; }
  .card--back .brand-mark__name { color: var(--card-white); font-size: 24px; }
</style>
</head>
<body>

<section class="card card--front" aria-label="Business card front">
  <div class="edge-band">
    <div class="edge-band__navy"></div>
    <div class="edge-band__gap"></div>
    <div class="edge-band__slate"></div>
  </div>
  <div class="name-tab"></div>

  <div class="identity">
    <h1 class="identity__name">Dana Whitfield</h1>
    <p class="identity__title">Chief Financial Officer</p>
    <div class="identity__rule"></div>
    <ul class="contact-list">
      <li class="contact-list__item">
        <svg class="contact-list__icon" viewBox="0 0 16 16"><circle cx="8" cy="8" r="7" fill="none" stroke="#cf2630" stroke-width="2"/><path d="M5.5 5.2c.6-.6 1.1-.4 1.4.2l.4.8c.2.4 0 .7-.3 1 .4.8 1 1.4 1.8 1.8.3-.3.6-.5 1-.3l.8.4c.6.3.8.8.2 1.4-.8.8-2.2.6-3.6-.8S4.7 6 5.5 5.2z" fill="#cf2630"/></svg>
        <span>(555) 817-3094</span>
      </li>
      <li class="contact-list__item">
        <svg class="contact-list__icon" viewBox="0 0 16 16"><rect x="1" y="3" width="14" height="10" fill="#cf2630"/><path d="M1 3l7 6 7-6" fill="none" stroke="#fff" stroke-width="1.2"/></svg>
        <span>dana.whitfield@larkridgemgmt.example</span>
      </li>
      <li class="contact-list__item">
        <svg class="contact-list__icon" viewBox="0 0 16 16"><circle cx="8" cy="8" r="7.5" fill="#cf2630"/><circle cx="8" cy="8" r="4" fill="none" stroke="#fff" stroke-width="1.2"/><path d="M4 8h8M8 4v8" stroke="#fff" stroke-width="1"/></svg>
        <span>larkridgemgmt.example</span>
      </li>
    </ul>
  </div>

  <div class="brand-mark">
    <span class="brand-mark__square"></span>
    <span class="brand-mark__name">Larkspur Ridge<br>Management</span>
  </div>
</section>

<section class="card card--back" aria-label="Business card back">
  <div class="brand-mark">
    <span class="brand-mark__square"></span>
    <span class="brand-mark__name">Larkspur Ridge Management</span>
  </div>
</section>

</body>
</html>
```